Law firm needs stationary and envelope design*

We would like to incorporate our logo into letterhead design and envelopes. We are looking for something that is moderately conservative but not old law firm style. Both the envelopes and the letterhead must have both firm addresses. We would like to incorporate the color of the logo, but only a small amount of color - perhaps on one of the borders. The addresses for the firm locations are listed below. Given that it is a law firm, it needs to somewhat conservative, but not the old school, small black font on cream colored paper design.

The firm addresses are:

27815 N. Harlow Pemberton Pkwy.
Ste 740
Scottsdale, AZ 85419

6208 E. Juniper Street
Ste 820
Burbank, CA 91873

Legal

Designer to choose colors to be used in the design.

• Both addresses:
• 27815 N. Harlow Pemberton Pkwy.
• Ste 740
• Scottsdale, AZ 85419
• 6208 E. Juniper Street
• Ste 820
• Burbank, CA 91873
• Small amount of color on border(s) that matches the logo but not too much color

```html
<!DOCTYPE html>
<html lang="en">
<head>
<meta charset="utf-8">
<title>Halvern Law – Envelope</title>
<link rel="stylesheet" href="https://fonts.googleapis.com/css2?family=Cinzel:wght@400&family=Lato:wght@400&display=swap">
<style>
  :root {
    --navy: #27215f;
    --paper: #ffffff;
    --window: #d9d9d9;
    --window-edge: #c4c4c4;
    --backdrop: #e4e4e6;
  }
  html, body {
    margin: 0;
    padding: 0;
    overflow: hidden;
  }
  .canvas {
    position: relative;
    width: 1200px;
    height: 1200px;
    background: var(--backdrop);
    overflow: hidden;
  }
  .envelope {
    position: absolute;
    left: 179px;
    width: 843px;
    height: 436px;
    background: var(--paper);
  }
  .envelope-front { top: 131px; }
  .envelope-back { top: 634px; }
  .envelope svg.shapes {
    position: absolute;
    inset: 0;
    width: 100%;
    height: 100%;
  }
  .band, .flap { fill: var(--navy); }
  .window {
    position: absolute;
    left: 399px;
    top: 214px;
    width: 369px;
    height: 163px;
    border-radius: 12px;
    background: var(--window);
    box-shadow: inset 0 0 0 2px var(--window-edge);
  }
  .firm-name {
    margin: 0;
    font-family: 'Cinzel', serif;
    font-weight: 400;
    color: var(--navy);
    letter-spacing: 0.5px;
    line-height: 1;
    white-space: nowrap;
  }
  .front-block {
    position: absolute;
    left: 29px;
    top: 38px;
  }
  .front-block .firm-name { font-size: 29px; }
  .addresses {
    margin: 12px 0 0 0;
    font-family: 'Lato', sans-serif;
    font-size: 13.5px;
    line-height: 20px;
    color: var(--navy);
    font-style: normal;
  }
  .addresses span { display: block; white-space: nowrap; }
  .back-name {
    position: absolute;
    left: 0;
    right: 0;
    top: 384px;
    text-align: center;
    font-size: 33px;
  }
</style>
</head>
<body>
<main class="canvas">

  <section class="envelope envelope-front" aria-label="Envelope front">
    <svg class="shapes" viewBox="0 0 843 436" aria-hidden="true">
      <polygon class="band band-top" points="0,0 445,0 426,19 0,19"/>
      <polygon class="band band-bottom" points="418,417 843,417 843,436 399,436"/>
    </svg>
    <div class="front-block">
      <h1 class="firm-name">Halvern Law</h1>
      <address class="addresses">
        <span>6208 E. Juniper Street, Ste 820, Burbank, CA 91873</span>
        <span>27815 N. Harlow Pemberton Pkwy.Ste 740, Scottsdale, AZ 85419</span>
      </address>
    </div>
    <div class="window" aria-label="Address window"></div>
  </section>

  <section class="envelope envelope-back" aria-label="Envelope back">
    <svg class="shapes" viewBox="0 0 843 436" aria-hidden="true">
      <path class="flap" d="M0,0 L843,0 L808,112 Q790,156 745,156 L95,156 Q55,156 36,114 Z"/>
    </svg>
    <p class="firm-name back-name">Halvern Law</p>
  </section>

</main>
</body>
</html>
```